Business Card Design Project

Please create a custom business card for Quenlow Capital. The logo is attached to this brief.

Also, here is the link to the logo design project: http://tasks.brivantolab.com/task.aspx?id=452673

Questions can be posted on the Discussion Board.

```html
<!DOCTYPE html>
<html lang="en">
<head>
<meta charset="utf-8">
<title>Quenlow Capital – Business Card</title>
<link rel="stylesheet" href="https://fonts.googleapis.com/css2?family=Source+Sans+3:wght@400;600;700&display=swap">
<style>
  :root {
    --page-bg: #e6e8ea;
    --card-blue: #2c4a83;
    --band-dark: #3b3b3d;
    --band-light: #ffffff;
    --text-light: #ffffff;
    --text-dark: #2a2a2c;
    --logo-blue: #3b63a8;
  }
  * { box-sizing: border-box; margin: 0; padding: 0; }
  html, body {
    width: 1200px; height: 1080px; overflow: hidden;
    background: var(--page-bg);
    font-family: "Source Sans 3", Arial, sans-serif;
  }
  .sheet {
    position: relative; width: 1200px; height: 1080px;
    display: flex; flex-direction: column; align-items: center;
    justify-content: center; gap: 40px;
  }
  .card {
    position: relative; width: 840px; height: 480px;
    background: var(--card-blue); overflow: hidden;
    box-shadow: 0 12px 30px rgba(0,0,0,0.25);
  }

  /* Brand lockup */
  .brand { display: flex; align-items: center; gap: 14px; }
  .brand-mark { width: 22px; height: 22px; background: currentColor; }
  .brand-name {
    font-weight: 600; letter-spacing: 4px; text-transform: uppercase;
    font-size: 30px; line-height: 1;
  }

  /* Front */
  .front .brand {
    position: absolute; top: 72px; left: 0; right: 0;
    justify-content: center; color: var(--text-light);
  }
  .holder {
    position: absolute; top: 178px; left: 0; right: 0;
    display: flex; flex-direction: column; align-items: center;
    color: var(--text-light);
  }
  .holder-name {
    font-weight: 700; font-size: 38px; padding: 0 26px 6px;
    border-bottom: 2px solid var(--text-light);
  }
  .holder-position {
    font-size: 24px; align-self: center; margin-left: 150px; margin-top: 6px;
  }
  .contact-band {
    position: absolute; left: 0; right: 0; bottom: 0; height: 150px;
    background: var(--band-dark); color: var(--text-light);
    display: grid; grid-template-columns: 1.25fr 1fr 1.15fr;
    align-items: center; padding: 0 40px; font-size: 18px;
  }
  .contact-group { display: flex; flex-direction: column; gap: 20px; }
  .contact-item { display: flex; align-items: center; gap: 14px; white-space: nowrap; }
  .contact-item svg { width: 22px; height: 22px; fill: var(--text-light); flex: none; }

  /* Back */
  .back .light-band {
    position: absolute; left: 0; top: 170px; width: 700px; height: 140px;
    background: var(--band-light);
    display: flex; align-items: center; justify-content: space-between;
    padding: 0 44px 0 50px;
  }
  .back .web { font-size: 26px; color: var(--text-dark); letter-spacing: 0.5px; }
  .back .brand { color: var(--text-dark); }
  .back .brand-mark { background: var(--logo-blue); }
  .back .brand-name { font-size: 28px; }
</style>
</head>
<body>
<main class="sheet">

  <section class="card front" aria-label="Business card front">
    <div class="brand">
      <span class="brand-mark"></span>
      <span class="brand-name">Quenlow Capital</span>
    </div>

    <div class="holder">
      <span class="holder-name">Your Long Name</span>
      <span class="holder-position">your position</span>
    </div>

    <div class="contact-band">
      <div class="contact-group">
        <div class="contact-item">
          <svg viewBox="0 0 24 24" aria-hidden="true"><path d="M12 2a7 7 0 0 0-7 7c0 5 7 13 7 13s7-8 7-13a7 7 0 0 0-7-7zm0 9.5A2.5 2.5 0 1 1 12 6.5a2.5 2.5 0 0 1 0 5z"/></svg>
          <span>Street No.123 &nbsp;Hometown</span>
        </div>
        <div class="contact-item">
          <svg viewBox="0 0 24 24" aria-hidden="true"><path d="M3 8c0-2 4-4 9-4s9 2 9 4v2h-4V8.5c-1.5-.6-3-.9-5-.9s-3.5.3-5 .9V10H3zM6 11h12l2 9H4z"/></svg>
          <span>+ 12.3456.7890</span>
        </div>
      </div>
      <div class="contact-group">
        <div class="contact-item">
          <svg viewBox="0 0 24 24" aria-hidden="true"><path d="M3 6h4v15H3zM9 3h10v6H9zm0 7h12v11H9zm3 3v2h2v-2zm4 0v2h2v-2zm-4 4v2h2v-2zm4 0v2h2v-2z"/></svg>
          <span>+ 12.3456.7890</span>
        </div>
        <div class="contact-item">
          <svg viewBox="0 0 24 24" aria-hidden="true"><path d="M7 2h10a1 1 0 0 1 1 1v18a1 1 0 0 1-1 1H7a1 1 0 0 1-1-1V3a1 1 0 0 1 1-1zm1 3v7h8V5zm0 9v2h2v-2zm3 0v2h2v-2zm3 0v2h2v-2zm-6 3v2h2v-2zm3 0v2h2v-2zm3 0v2h2v-2z"/></svg>
          <span>+ 12.3456.7890</span>
        </div>
      </div>
      <div class="contact-group">
        <div class="contact-item">
          <svg viewBox="0 0 24 24" aria-hidden="true"><path d="M2 5h20v14H2zm2 2v.5l8 5.5 8-5.5V7l-8 5.2z"/></svg>
          <span>yourname@company.com</span>
        </div>
        <div class="contact-item">
          <svg viewBox="0 0 24 24" aria-hidden="true"><path d="M12 3l10 9h-3v9h-5v-6h-4v6H5v-9H2z"/></svg>
          <span>www.company.com</span>
        </div>
      </div>
    </div>
  </section>

  <section class="card back" aria-label="Business card back">
    <div class="light-band">
      <span class="web">www.company.com</span>
      <div class="brand">
        <span class="brand-mark"></span>
        <span class="brand-name">Quenlow Capital</span>
      </div>
    </div>
  </section>

</main>
</body>
</html>
```